BrindleCourt Risk & Planning Biz cards

**BrindleCourt Risk & Planning – Premium Business Card Design**

I am seeking a professional designer to create a luxury double-sided business card for BrindleCourt Risk & Planning, a retirement and wealth planning firm focused on helping families preserve wealth, reduce unnecessary taxes, protect assets, and create lasting legacies.

The card should reflect the image of a boutique wealth advisory firm or family office—not a traditional insurance salesperson. The overall feel should communicate trust, sophistication, stability, integrity, and long-term relationships.

**Brand Direction**

* Use the provided BrindleCourt Risk & Planning logo and brand assets.
* Color palette should be based on BrindleCourt's deep forest green, gold accents, and neutral tones.
* Design should be clean, elegant, and timeless.
* Avoid cluttered layouts, stock imagery, or overly aggressive sales-oriented designs.
* Emphasize premium whitespace and strong typography.

**Card Specifications**

* Standard U.S. business card size (3.5" x 2")
* Double-sided design
* Full-bleed print-ready files
* CMYK color format
* Include editable source files (AI, PSD, Canva, or similar)

**Preferred Print Finish**
The design should be optimized for:

* Velvet (soft-touch) finish
* Gold foil logo and accent elements
* Standard square corners
* Optional gold-painted edge compatibility if desired

**Front Side**

* BrindleCourt Risk & Planning logo prominently displayed
* Minimalist, high-end appearance
* Focus on branding and visual impact rather than excessive text

**Back Side**
Include:

* Derrin Holloway
* Founder & Financial Professional
* Phone Number
* Email Address
* QR Code (website or appointment scheduling page)

**Overall Inspiration**
Think:

* Private wealth management firm
* Boutique family office
* Estate planning attorney
* High-end financial advisory practice

The finished design should feel premium, memorable, and trustworthy while remaining understated and professional. The goal is for clients to immediately associate the BrindleCourt brand with confidence, stewardship, and long-term financial guidance.

Printer template for foil https://www.prestaxmail.example/print-templates/foil-business-cards/

Target Market(s)

Foil should be used strategically on the BrindleCourt logo and select design elements. Deep forest green background with gold foil accents. Luxury wealth management / family office aesthetic. Clean, minimalist layout with ample whitespace. Professional and timeless appearance suitable for affluent clients and business owners.

Industry/Entity Type

Financial Services / Wealth Advisor

Contact Information for Business Card

* Derrin Holloway * Founder & Financial Professional * Phone Number * Email Address * Website * QR Code (website or appointment scheduling page)

Requirements
Must have
• Design must be optimized for Raised Gold Foil on Silk business cards.

```html
<!DOCTYPE html>
<html lang="en">
<head>
<meta charset="utf-8">
<title>BrindleCourt Risk &amp; Planning — Business Cards</title>
<link rel="stylesheet" href="https://fonts.googleapis.com/css2?family=Questrial&family=Cabin+Condensed:wght@400&display=swap">
<style>
  :root {
    --page: #ffffff;
    --card-light: #ffffff;
    --forest: #2a321f;
    --gold: #c8a14f;
    --gold-soft: #d4c07a;
    --ink: #141210;
    --shadow: rgba(0, 0, 0, 0.16);
  }
  * { margin: 0; padding: 0; box-sizing: border-box; }
  html, body { width: 960px; height: 1200px; overflow: hidden; background: var(--page); }
  .sheet { position: relative; width: 960px; height: 1200px; }
  .card {
    position: absolute; left: 266px; width: 444px; height: 250px;
    box-shadow: 0 4px 18px var(--shadow); overflow: hidden;
    font-family: "Questrial", sans-serif;
  }
  .card--front-light { top: 50px; background: var(--card-light); color: var(--ink); }
  .card--back-light { top: 338px; background: var(--card-light); color: var(--ink); }
  .card--back-dark { top: 628px; background: var(--forest); color: var(--gold-soft); }
  .card--front-dark { top: 910px; background: var(--forest); color: var(--gold); }

  .brand { position: absolute; text-align: center; }
  .brand__mark { display: block; margin: 0 auto 12px; width: 40px; height: 40px; border-radius: 50%; background: currentColor; }
  .brand__name { font-size: 30px; line-height: 1; letter-spacing: -0.5px; }
  .brand__tag { font-size: 9px; letter-spacing: 2.6px; margin-top: 6px; }

  .card--front-light .brand, .card--front-dark .brand { left: 0; right: 0; top: 56px; }
  .card--back-light .brand { left: 20px; top: 32px; text-align: left; }
  .card--back-light .brand__name { font-size: 27px; }
  .card--back-dark .brand { left: 10px; width: 124px; top: 72px; color: var(--gold); }
  .card--back-dark .brand__name { font-size: 21px; }
  .card--back-dark .brand__tag { font-size: 7px; letter-spacing: 1.6px; }

  .person { position: absolute; text-align: center; }
  .person__name { font-size: 24px; line-height: 1; }
  .person__role { font-size: 11px; letter-spacing: 1px; margin-top: 4px; }
  .card--back-light .person { left: 20px; top: 117px; }
  .card--back-dark .person { left: 172px; top: 122px; }

  .contacts { position: absolute; left: 19px; top: 186px; list-style: none;
    font-family: "Cabin Condensed", sans-serif; font-size: 9.6px; }
  .contacts li { display: flex; align-items: center; height: 18.5px; }
  .contacts svg { width: 14px; height: 14px; margin-right: 6px; flex: none; }
  .card--back-light .contacts { color: var(--ink); }
  .card--back-dark .contacts { color: var(--gold-soft); }
</style>
</head>
<body>
<main class="sheet">

  <section class="card card--front-light">
    <div class="brand">
      <span class="brand__mark"></span>
      <div class="brand__name">BrindleCourt</div>
      <div class="brand__tag">RISK &amp; PLANNING</div>
    </div>
  </section>

  <section class="card card--back-light">
    <div class="brand">
      <div class="brand__name">BrindleCourt</div>
      <div class="brand__tag">RISK &amp; PLANNING</div>
    </div>
    <div class="person">
      <div class="person__name">Derrin Holloway</div>
      <div class="person__role">CEO</div>
    </div>
    <ul class="contacts">
      <li><svg viewBox="0 0 14 14" fill="none" stroke="currentColor" stroke-width="0.9"><circle cx="7" cy="7" r="6.3"/><rect x="3.6" y="4.8" width="6.8" height="4.6"/><path d="M3.6 4.8 7 7.6l3.4-2.8"/></svg>dholloway@brindlecourt.example</li>
      <li><svg viewBox="0 0 14 14" fill="none" stroke="currentColor" stroke-width="0.9"><circle cx="7" cy="7" r="6.3"/><path d="M7 11 4.6 6.8a2.5 2.5 0 1 1 4.8 0Z"/><circle cx="7" cy="5.6" r="0.9"/></svg>24 Harrow Ln., Millbrook, MA 01500</li>
      <li><svg viewBox="0 0 14 14" fill="none" stroke="currentColor" stroke-width="0.9"><circle cx="7" cy="7" r="6.3"/><circle cx="7" cy="7" r="4"/><path d="M3 7h8M7 3v8M4 5h6M4 9h6"/></svg>555 01 23 456 · www.brindlecourt.example</li>
    </ul>
  </section>

  <section class="card card--back-dark">
    <div class="brand">
      <div class="brand__name">BrindleCourt</div>
      <div class="brand__tag">RISK &amp; PLANNING</div>
    </div>
    <div class="person">
      <div class="person__name">Derrin Holloway</div>
      <div class="person__role">CEO</div>
    </div>
    <ul class="contacts">
      <li><svg viewBox="0 0 14 14" fill="none" stroke="currentColor" stroke-width="0.9"><circle cx="7" cy="7" r="6.3"/><rect x="3.6" y="4.8" width="6.8" height="4.6"/><path d="M3.6 4.8 7 7.6l3.4-2.8"/></svg>dholloway@brindlecourt.example</li>
      <li><svg viewBox="0 0 14 14" fill="none" stroke="currentColor" stroke-width="0.9"><circle cx="7" cy="7" r="6.3"/><path d="M7 11 4.6 6.8a2.5 2.5 0 1 1 4.8 0Z"/><circle cx="7" cy="5.6" r="0.9"/></svg>24 Harrow Ln., Millbrook, MA 01500</li>
      <li><svg viewBox="0 0 14 14" fill="none" stroke="currentColor" stroke-width="0.9"><circle cx="7" cy="7" r="6.3"/><circle cx="7" cy="7" r="4"/><path d="M3 7h8M7 3v8M4 5h6M4 9h6"/></svg>555 01 23 456 · www.brindlecourt.example</li>
    </ul>
  </section>

  <section class="card card--front-dark">
    <div class="brand">
      <span class="brand__mark"></span>
      <div class="brand__name">BrindleCourt</div>
      <div class="brand__tag">RISK &amp; PLANNING</div>
    </div>
  </section>

</main>
</body>
</html>
```